Infografiken für Lösungen für Gebäudeautomation
Zielgruppe
'Der Name lumora steht für massgeschneiderte Lösungen für die Gebäudeautomation. «Nachhaltige und wirtschaftliche Produkte sind uns wichtig». Die Qualität unserer Produkte und Dienstleistungen stehen stets im Vordergrund und bilden das Fundament für eine zufriedene Kundschaft.'
bitte informieren Sie sich unter www.lumora-beispiel.ch
Aufgabenstellung
Es gibt keine Formatvorgaben. In dieser Infografik soll ersichtlich sein, welche Dienstleistungen wir unsere Kunden anbieten. Im dem Sinne alles auf einem Blick:
Ich weiss was die Firma macht
ich weiss, welche Werte die Firma vertritt
ich weiss, wie ich die Firma kontaktieren kann
Das Farblayout ist unter www.lumora-beispiel.ch ersichtlich

```html
<!DOCTYPE html>
<html lang="de">
<head>
<meta charset="utf-8">
<title>lumora – Gebäudeautomation auf einen Blick</title>
<link rel="stylesheet" href="https://fonts.googleapis.com/css2?family=Noto+Sans:wght@400;700;800&display=swap">
<style>
  :root{
    --green:#2f9a3a;
    --green-box:#339636;
    --heading:#5b5b5b;
    --text:#555;
    --line:#bdbdbd;
    --circle:#ececec;
    --paper:#ffffff;
  }
  *{box-sizing:border-box;margin:0;padding:0}
  html,body{width:1200px;height:797px;overflow:hidden;background:var(--paper)}
  body{font-family:"Noto Sans",sans-serif;color:var(--text);position:relative}
  .abs{position:absolute;white-space:nowrap}
  .icon-circle{position:absolute;width:40px;height:40px;border-radius:50%;background:var(--circle);display:flex;align-items:center;justify-content:center}
  .kicker{font-size:9px;font-weight:700;color:var(--green);letter-spacing:.4px;line-height:12px}
  .title{font-size:12.5px;font-weight:700;color:var(--heading);letter-spacing:.5px;line-height:16.5px}
  .lead{font-size:9.8px;font-weight:700;color:var(--green);line-height:12.6px}
  .subhead{font-size:9.5px;font-weight:700;color:var(--heading);letter-spacing:.4px;line-height:12px}
  .rule{position:absolute;height:1px;background:var(--line)}
  .vrule{position:absolute;width:1px;background:var(--line)}
  .checklist{list-style:none;font-size:9.5px;line-height:12.2px;color:var(--text);white-space:nowrap}
  .checklist li{position:relative;padding-left:11px}
  .checklist li::before{content:"";position:absolute;left:1px;top:2px;width:3px;height:6px;border:solid var(--green);border-width:0 1.6px 1.6px 0;transform:rotate(45deg)}
  .brand{position:absolute;left:893px;top:110px;width:126px;text-align:center}
  .brand-name{font-size:28px;font-weight:800;color:var(--green);letter-spacing:1.5px;line-height:32px}
  .brand-tag{font-size:5.6px;color:var(--heading);letter-spacing:.1px;line-height:8px;white-space:nowrap}
  .building{position:absolute;left:453px;top:142px;width:294px;height:305px;
    background:linear-gradient(165deg,#55b463 0%,#e8e9f2 48%,#a9cf3f 100%);
    clip-path:polygon(18% 25.5%,63.9% 0%,84.7% 11.8%,100% 64.6%,38.4% 100%,0% 78.4%,5.1% 61.6%,18% 61.6%)}
  .claim-box{position:absolute;left:182px;top:530px;width:194px;height:151px;background:var(--green-box);color:#fff}
  .claim-list{position:absolute;left:15px;top:13px;list-style:none;font-size:15px;font-weight:800;line-height:17.4px;letter-spacing:.5px}
  .claim-list li{position:relative;padding-left:18px}
  .claim-list li::before{content:"";position:absolute;left:3px;top:3px;width:4px;height:8px;border:solid #fff;border-width:0 2px 2px 0;transform:rotate(45deg)}
  .claim-sub{position:absolute;left:15px;top:643px;font-size:8px;font-weight:700;line-height:12.5px;letter-spacing:.3px;color:#fff;white-space:nowrap}
  .contact-lines{font-size:9.6px;line-height:12.3px;color:var(--text)}
  .contact-lines .company{color:var(--green);font-weight:700}
  .contact-row{display:flex;align-items:center;gap:6px;font-size:9.6px;line-height:12.4px}
  .web{position:absolute;left:880px;width:138px;text-align:right;top:671px;font-size:10.5px;font-weight:700;color:var(--green);line-height:14px}
</style>
</head>
<body>

  <div class="brand">
    <div class="brand-name">LUMORA</div>
    <div class="brand-tag">AUTOMATION•VISUALISIERUNG•HLKSE</div>
  </div>

  <div class="building" role="img" aria-label="Isometrische Illustration eines Bürogebäudes mit grünem Dach, Eingangsbereich und zwei Bäumen auf einer Rasenfläche"></div>

  <!-- Ziele -->
  <div class="icon-circle" style="left:224px;top:136px">
    <svg width="18" height="18" viewBox="0 0 24 24" aria-hidden="true"><path d="M5 19 L17 7 M10 7 H17 V14" fill="none" stroke="#2f9a3a" stroke-width="3" stroke-linecap="round" stroke-linejoin="round"/></svg>
  </div>
  <div class="abs kicker" style="left:274px;top:141px">HOCH HINAUS</div>
  <div class="abs title" style="left:274px;top:154px">UNSERE ZIELE</div>
  <div class="rule" style="left:392px;top:162px;width:186px"></div>
  <div class="abs lead" style="left:274px;top:182px">Lorem ipsum dolor sit amet!</div>
  <ul class="abs checklist" style="left:274px;top:206px">
    <li>Bea voluptatibus sit dolorrum volum<br>arum alitatur, ipsaniae. Itatum reperio<br>reicia verna lorem ipsum dolor</li>
    <li>Wui duntese quatur, siti corecup scit<br>ulla nia pos moluptatur sitatect</li>
    <li>Bea voluptatibus sit dolorrum volum<br>arum alitatur, ipsaniae. Itatum er</li>
  </ul>

  <!-- Werte -->
  <div class="icon-circle" style="left:182px;top:338px">
    <svg width="18" height="18" viewBox="0 0 24 24" aria-hidden="true"><path d="M13 4 L20 4 L20 11 L12 15 L9 12 Z" fill="#2f9a3a"/><path d="M10 14 L5 19" stroke="#2f9a3a" stroke-width="3" stroke-linecap="round"/></svg>
  </div>
  <div class="abs kicker" style="left:233px;top:344px">DAS FUNDAMENT</div>
  <div class="abs title" style="left:233px;top:357px">UNSERE WERTE</div>
  <div class="rule" style="left:350px;top:366px;width:98px"></div>
  <div class="abs lead" style="left:233px;top:384px">Nachhaltige und wirtschaftliche<br>Produkte sind unser Markenzeichen.</div>
  <ul class="abs checklist" style="left:233px;top:421px">
    <li>LUMORA steht für massgeschneiderte<br>Lösungen für die Gebäudeautomation</li>
    <li>Die Qualität unserer Produkte und Dienstleistungen<br>stehen stets im Vordergrund und bilden das<br>Fundament für eine zufriedene Kundschaft</li>
  </ul>

  <!-- Claim box -->
  <div class="claim-box">
    <ul class="claim-list">
      <li>AUTOMATION</li>
      <li>VISUALISIERUNG</li>
      <li>HLKSE</li>
    </ul>
  </div>
  <div class="claim-sub" style="left:197px">SMARTE UND SIMPLE AUTOMATION<br>FÜR DAS GEBÄUDE</div>

  <!-- Kontakt -->
  <div class="vrule" style="left:591px;top:444px;height:25px"></div>
  <div class="icon-circle" style="left:571px;top:477px">
    <svg width="19" height="14" viewBox="0 0 24 18" aria-hidden="true"><rect x="1.5" y="1.5" width="21" height="15" fill="none" stroke="#2f9a3a" stroke-width="2"/><path d="M2 2 L12 10 L22 2 M2 16 L9 9 M22 16 L15 9" fill="none" stroke="#2f9a3a" stroke-width="2"/></svg>
  </div>
  <div class="abs kicker" style="left:569px;top:529px">KONTAKT</div>
  <div class="abs title" style="left:569px;top:542px">UNSERE TÜRE STEHT<br>IHNEN OFFEN</div>
  <div class="abs contact-lines" style="left:569px;top:586px">
    <div class="company">lumora automation GmbH</div>
    <div>Lindenweg 12</div>
    <div>8000 Musterdorf</div>
  </div>
  <div class="abs" style="left:569px;top:634px">
    <div class="contact-row">
      <svg width="10" height="10" viewBox="0 0 12 12" aria-hidden="true"><circle cx="6" cy="6" r="6" fill="#2f9a3a"/><path d="M4 3 L5 5 L4.5 6 Q5.5 7.5 6.5 7.5 L7.5 7 L9 8.5 Q8 9.5 6.5 9.3 Q3.2 8.3 2.8 4.5 Q3 3.3 4 3Z" fill="#fff"/></svg>
      <span>+41 44 000 12 34</span>
    </div>
    <div class="contact-row">
      <svg width="10" height="10" viewBox="0 0 12 12" aria-hidden="true"><circle cx="6" cy="6" r="6" fill="#2f9a3a"/><rect x="3" y="4" width="6" height="4.2" fill="#fff"/><path d="M3 4 L6 6.3 L9 4" fill="none" stroke="#2f9a3a" stroke-width=".8"/></svg>
      <span>info@lumora-beispiel.ch</span>
    </div>
  </div>

  <!-- Leistungen -->
  <div class="rule" style="left:716px;top:212px;width:25px"></div>
  <div class="icon-circle" style="left:751px;top:192px">
    <svg width="20" height="17" viewBox="0 0 26 22" aria-hidden="true"><g fill="#2f9a3a"><rect x="6" y="2" width="14" height="5"/><rect x="1" y="9" width="11" height="5"/><rect x="14" y="9" width="11" height="5"/><rect x="6" y="16" width="14" height="5"/></g></svg>
  </div>
  <div class="abs kicker" style="left:805px;top:200px">STEIN AUF STEIN</div>
  <div class="abs title" style="left:805px;top:213px">UNSERE LEISTUNGEN</div>

  <div class="abs subhead" style="left:805px;top:240px">GEBÄUDEAUTOMATION</div>
  <ul class="abs checklist" style="left:805px;top:265px">
    <li>Planungsunterstützung</li>
    <li>Gebäudeautomation / Raumautomation</li>
    <li>Intelligentes Wohnen durch Smart Home</li>
    <li>Schemata und Prinzipschemas</li>
    <li>Programmierung und Integration uvm.</li>
  </ul>

  <div class="abs subhead" style="left:805px;top:337px">VISUALISIERUNG</div>
  <ul class="abs checklist" style="left:805px;top:362px">
    <li>Überwachung der Anlagen</li>
    <li>Kontrolle diskreter und<br>kontinuierlicher Prozesse</li>
    <li>Datenerfassung via Datenserver</li>
    <li>Alarmierung mit Kategorisierung uvm.</li>
  </ul>

  <div class="abs subhead" style="left:805px;top:435px">HLKSE ANLAGEAUTOMATION (MSR)</div>
  <ul class="abs checklist" style="left:805px;top:460px">
    <li>Ingenieurtechnische Leistungen</li>
    <li>Schaltschranklayout und Aufbau</li>
    <li>Programmierung der Automation</li>
    <li>Inbetriebnahme</li>
    <li>Dokumentation uvm.</li>
  </ul>

  <div class="abs subhead" style="left:805px;top:532px">SPEZIELLE DIENSTLEISTUNGEN</div>
  <ul class="abs checklist" style="left:805px;top:557px">
    <li>Bauherrenberatung und<br>Qualitätssicherung</li>
    <li>Schulung für das Facility Management</li>
    <li>Anlageinstruktionen und Weiterbildungen</li>
    <li>Gebäudetechnische Störanleitungen uvm.</li>
  </ul>

  <div class="web">www.lumora-beispiel.ch</div>

</body>
</html>
```